Business Card & Stationary for Orthodontic Office
Lena Voss Orthodontics
Business Card & Stationary for Orthodontic Office  - Medical
Creative Brief
Professional
See Additional Comments
4127 Marlow Ct Ashbrook, NY 14398
Info@SmileCraftClinics.com
www.SmileCraftClinics.com
The logo contains our DBA name however below should read smaller; Lena Voss D.M.D. M.S. PC Also the NCT attached should be included as well.
(additional locations) Pinecrest 5193 Hollin Ridge Ave. Pinecrest, NY 14387 (716)555-0193 Dunmore Falls 2615 Fenwick Rd. Dunmore Falls, NY 14391 (716)555-0147 Kelderton 58 Lorimer St. Kelderton, NY 14802 (585)555-0126 Harlow Bend 4712 W. Tarrow St. Harlow Bend, NY 14906 (585)555-0126
LVBrace LVBrace
*************EDIT TO BRIEF*************** We are no longer requiring the NCT logo instead under Lena Voss D.M.D. M.S. PC it should say; "Board Certified Orthodontist" Obviously this is without the quotations. Also the back side of the business card MUST include the remaining office locations. If your draft is submitted without this information on the back it WILL BE ELIMINATED!
*****PLEASE READ THE BRIEF BEFORE SUBMITTING DESIGNS AS THE NCT LOGO MUST BE INCLUDED******** We need all new office supplies as one of our doctors has retired. Business cards (front and back) Stationary (letterhead, envelopes #10, large flat envelopes 12"x15") Included in the brief is a copy of our current letterhead and business card (front & back) to be used as a base point. Our remaining doctor is young, professional, and very modern. Please let this be reflected in the designs that you present.

```html
<!DOCTYPE html>
<html lang="en">
<head>
<meta charset="utf-8">
<title>Lena Voss Orthodontics — Business Cards</title>
<link rel="stylesheet" href="https://fonts.googleapis.com/css2?family=Open+Sans:wght@400;600;700&display=swap">
<style>
  :root {
    --bg: #e9ebee;
    --white: #ffffff;
    --green: #6cc52c;
    --green-light: #9ade3e;
    --blue: #1f8fd8;
    --blue-light: #3fb2ef;
    --text-muted: #5d6b77;
    --accent-blue: #1f8fd8;
    --accent-green: #6cc52c;
  }
  * { margin: 0; padding: 0; box-sizing: border-box; }
  html, body { width: 1200px; height: 1104px; overflow: hidden; }
  body {
    background: var(--bg);
    font-family: "Open Sans", Arial, sans-serif;
    position: relative;
  }
  .card {
    position: absolute;
    width: 560px;
    height: 320px;
    border-radius: 16px;
    overflow: hidden;
    box-shadow: 0 8px 24px rgba(0,0,0,0.18);
  }
  .card-front { left: 320px; top: 70px; background: var(--white); }
  .card-back-green { left: 20px; top: 470px; background: linear-gradient(160deg, var(--green-light), var(--green)); color: var(--white); }
  .card-back-blue { left: 620px; top: 470px; background: linear-gradient(160deg, var(--blue-light), var(--blue)); color: var(--white); }

  /* front */
  .front-mark { position: absolute; left: 32px; top: 34px; display: flex; align-items: center; gap: 12px; }
  .mark-dot { width: 38px; height: 38px; border-radius: 50%; background: var(--accent-blue); flex: none; }
  .front-name { font-size: 26px; font-weight: 600; color: var(--accent-blue); letter-spacing: 0.5px; }
  .front-rule { position: absolute; left: 32px; top: 92px; width: 300px; height: 2px; background: var(--accent-green); }
  .front-shade { position: absolute; right: 0; top: 0; width: 260px; height: 320px; background: linear-gradient(120deg, rgba(255,255,255,0) 30%, rgba(108,197,44,0.10) 100%); }
  .doctor { position: absolute; left: 90px; top: 112px; font-size: 14px; font-weight: 600; color: var(--accent-blue); }
  .address { position: absolute; left: 90px; top: 144px; font-size: 12px; line-height: 17px; color: var(--text-muted); }
  .contact { position: absolute; left: 90px; top: 190px; list-style: none; font-size: 12px; line-height: 20px; color: var(--text-muted); }
  .contact li { display: flex; align-items: center; gap: 8px; }
  .contact svg { width: 12px; height: 12px; fill: var(--accent-blue); flex: none; }

  /* back */
  .back-mark { position: absolute; left: 28px; top: 26px; display: flex; align-items: center; gap: 8px; font-size: 12px; font-weight: 600; }
  .back-mark .mark-dot { width: 22px; height: 22px; background: var(--white); }
  .locations-title { position: absolute; left: 28px; top: 190px; font-size: 15px; font-weight: 700; }
  .locations { position: absolute; left: 28px; top: 222px; right: 20px; display: grid; grid-template-columns: repeat(4, 1fr); gap: 10px; font-size: 10.5px; line-height: 15px; }
  .location-name { font-weight: 700; }
</style>
</head>
<body>

<section class="card card-front" aria-label="Business card front">
  <div class="front-shade"></div>
  <div class="front-mark">
    <span class="mark-dot"></span>
    <span class="front-name">Lena Voss Orthodontics</span>
  </div>
  <div class="front-rule"></div>
  <p class="doctor">Lena Voss D.M.D. M.S. PC</p>
  <p class="address">4127 Marlow Ct<br>Ashbrook, NY 14398</p>
  <ul class="contact">
    <li><svg viewBox="0 0 24 24"><path d="M6.6 10.8a15 15 0 006.6 6.6l2.2-2.2a1 1 0 011-.25 11.4 11.4 0 003.6.57 1 1 0 011 1V20a1 1 0 01-1 1A17 17 0 013 4a1 1 0 011-1h3.5a1 1 0 011 1c0 1.25.2 2.45.57 3.6a1 1 0 01-.25 1z"/></svg>(716)555-0162</li>
    <li><svg viewBox="0 0 24 24"><rect x="3" y="8" width="18" height="10" rx="2"/><rect x="7" y="3" width="10" height="5"/></svg>(716)555-0178</li>
    <li><svg viewBox="0 0 24 24"><path d="M2 5h20v14H2z"/></svg>Info@SmileCraftClinics.com</li>
    <li><svg viewBox="0 0 24 24"><circle cx="12" cy="12" r="10"/></svg>www.SmileCraftClinics.com</li>
  </ul>
</section>

<section class="card card-back-green" aria-label="Business card back, green">
  <div class="back-mark"><span class="mark-dot"></span><span>Lena Voss Orthodontics</span></div>
  <h2 class="locations-title">Other Locations</h2>
  <div class="locations">
    <div><div class="location-name">Dunmore Falls</div>2615 Fenwick Rd.<br>Dunmore Falls, NY 14391<br>(716)555-0147</div>
    <div><div class="location-name">Kelderton</div>58 Lorimer St.<br>Kelderton, NY 14802<br>(585)555-0126</div>
    <div><div class="location-name">Pinecrest</div>5193 Hollin Ridge Ave.<br>Pinecrest, NY 14387<br>(716)555-0193</div>
    <div><div class="location-name">Harlow Bend</div>4712 W. Tarrow St.<br>Harlow Bend, NY 14906<br>(585)555-0126</div>
  </div>
</section>

<section class="card card-back-blue" aria-label="Business card back, blue">
  <div class="back-mark"><span class="mark-dot"></span><span>Lena Voss Orthodontics</span></div>
  <h2 class="locations-title">Other Locations</h2>
  <div class="locations">
    <div><div class="location-name">Dunmore Falls</div>2615 Fenwick Rd.<br>Dunmore Falls, NY 14391<br>(716)555-0147</div>
    <div><div class="location-name">Kelderton</div>58 Lorimer St.<br>Kelderton, NY 14802<br>(585)555-0126</div>
    <div><div class="location-name">Pinecrest</div>5193 Hollin Ridge Ave.<br>Pinecrest, NY 14387<br>(716)555-0193</div>
    <div><div class="location-name">Harlow Bend</div>4712 W. Tarrow St.<br>Harlow Bend, NY 14906<br>(585)555-0126</div>
  </div>
</section>

</body>
</html>
```